Bellcrest HVAC Business Card design

Looking for a modern professional two sided design. Showing contact info and services provided. Possibly on a silk card stock.
Using blues or greens or greys and maybe metallic. One color or a mixture of these.
Dorian Vance
dvance@bellcresthvac-example.net
555-318-4702
Air Conditioning
Heating
Heat Pumps / Gas / Oil
Ductless mini splits
Controls
VFD's
Pumps
Gas Fitting/Piping
Service and New install
Residential / Commercial
Industry/Entity Type
Mechanical HVAC
Contact Information for Business Card
Logo, contact info and provided services

```html
<!DOCTYPE html>
<html lang="en">
<head>
<meta charset="utf-8">
<title>Bellcrest HVAC Business Card</title>
<link rel="stylesheet" href="https://fonts.googleapis.com/css2?family=Montserrat:wght@500;600;700;800&display=swap">
<style>
  :root {
    --stage: #1c1c1d;
    --card-grey: #6a6b6d;
    --card-edge: #7a7b7d;
    --silver-light: #e4e5e7;
    --silver-mid: #a9abae;
    --silver-dark: #55575a;
    --brand-blue: #0f55b4;
    --ink-white: #f4f5f7;
  }
  * { box-sizing: border-box; margin: 0; padding: 0; }
  html, body { width: 1200px; height: 875px; overflow: hidden; }
  body {
    background: radial-gradient(circle at 50% 45%, #2a2a2b 0%, var(--stage) 70%);
    font-family: "Montserrat", sans-serif;
    position: relative;
  }
  .card {
    position: absolute;
    top: 283px;
    width: 540px;
    height: 310px;
    border-radius: 22px;
    background: var(--card-grey);
    border: 1px solid var(--card-edge);
    overflow: hidden;
    box-shadow: 0 18px 40px rgba(0,0,0,.55);
  }
  .card--back { left: 40px; }
  .card--front { left: 620px; }

  /* back side */
  .brand-pattern {
    position: absolute; inset: 0;
    background: linear-gradient(135deg, #8d8f92 0%, #b7b9bc 30%, #6f7073 55%, #a3a5a8 80%, #7c7e81 100%);
    opacity: .85;
  }
  .services-band {
    position: absolute;
    left: 150px; right: 0;
    top: 104px; height: 122px;
    background: var(--brand-blue);
    border-radius: 61px 0 0 61px;
    display: flex; flex-direction: column; justify-content: center; align-items: center;
    color: var(--ink-white);
    font-size: 13px; font-weight: 500; line-height: 1.55;
    text-align: center;
    padding-left: 20px;
  }

  /* front side */
  .brand-mark {
    position: absolute;
    left: 34px; top: 112px;
    display: flex; align-items: center; gap: 10px;
  }
  .brand-mark__dot {
    width: 34px; height: 34px; border-radius: 50%;
    background: var(--silver-light);
  }
  .brand-mark__name {
    color: var(--silver-light);
    font-weight: 800; font-size: 22px; letter-spacing: .5px;
  }
  .brand-emblem {
    position: absolute;
    left: 300px; top: 26px;
    width: 220px; height: 220px; border-radius: 50%;
    background: radial-gradient(circle at 35% 30%, var(--silver-light) 0%, var(--silver-mid) 45%, var(--silver-dark) 100%);
  }
  .contact {
    position: absolute; left: 34px; top: 200px;
  }
  .contact__name {
    color: var(--brand-blue);
    font-weight: 800; font-size: 27px; margin-bottom: 10px;
  }
  .contact__line {
    display: flex; align-items: center; gap: 9px;
    color: var(--ink-white); font-size: 13px; margin-top: 6px;
  }
  .contact__line--phone { font-weight: 700; font-size: 15px; }
  .contact__icon {
    width: 20px; height: 20px; border-radius: 50%;
    background: var(--brand-blue);
    display: flex; align-items: center; justify-content: center;
  }
</style>
</head>
<body>
  <section class="card card--back" aria-label="Card back: services">
    <div class="brand-pattern" role="img" aria-label="Repeating silver foil brand emblem pattern"></div>
    <div class="services-band">
      <p>• Air Conditioning • Heating • Heat Pumps / Gas / Oil</p>
      <p>• Ductless mini splits • Controls • VFD's • Pumps</p>
      <p>• Gas Fitting/Piping • Service and New install</p>
      <p>• Residential / Commercial</p>
    </div>
  </section>

  <section class="card card--front" aria-label="Card front: contact">
    <div class="brand-mark">
      <span class="brand-mark__dot"></span>
      <span class="brand-mark__name">Bellcrest HVAC</span>
    </div>
    <div class="brand-emblem" role="img" aria-label="Large silver foil brand emblem"></div>
    <div class="contact">
      <p class="contact__name">Dorian Vance</p>
      <p class="contact__line">
        <span class="contact__icon">
          <svg width="12" height="9" viewBox="0 0 12 9"><rect x=".5" y=".5" width="11" height="8" fill="none" stroke="#fff"/><path d="M.5 .5 6 5l5.5-4.5" fill="none" stroke="#fff"/></svg>
        </span>
        dvance@bellcresthvac-example.net
      </p>
      <p class="contact__line contact__line--phone">
        <span class="contact__icon">
          <svg width="11" height="11" viewBox="0 0 24 24"><path fill="#fff" d="M6.6 10.8a15 15 0 0 0 6.6 6.6l2.2-2.2a1 1 0 0 1 1-.25 11.4 11.4 0 0 0 3.6.57 1 1 0 0 1 1 1V20a1 1 0 0 1-1 1A17 17 0 0 1 3 4a1 1 0 0 1 1-1h3.5a1 1 0 0 1 1 1c0 1.25.2 2.45.57 3.6a1 1 0 0 1-.25 1z"/></svg>
        </span>
        555-318-4702
      </p>
    </div>
  </section>
</body>
</html>
```